Business Card Design

We are looking for a double sided business card.

On one side would be our logo

On the Other Side

Martin Kolby
Sales and Marketing

Phone/Text Logo and 530-418-2763
Email Logo and info@plumvalepets.com
Website Logo and www.plumvalepets.com
Facebook Logo and plumvale pets
Instagram Logo and plumvale_pets

Target Market(s)

Pet owners

Contact Information for Business Card

In project description

Requirements
Must have
• Logo

```html
<!DOCTYPE html>
<html lang="en">
<head>
<meta charset="utf-8">
<title>Plumvale Pets — Business Card</title>
<link rel="stylesheet" href="https://fonts.googleapis.com/css2?family=Montserrat:wght@400;500;600&display=swap">
<style>
  :root {
    --bg: #2a2a2a;
    --card-black: #1c1c1e;
    --ink: #141414;
    --gold: #f0c22c;
    --orange: #e8782c;
    --silver: #d9d9d9;
    --silver-dark: #8a8a8a;
    --emboss: #333335;
  }
  * { box-sizing: border-box; margin: 0; padding: 0; }
  html, body { width: 1200px; height: 1015px; overflow: hidden; }
  body {
    background: var(--bg);
    font-family: "Montserrat", sans-serif;
    position: relative;
  }
  .card {
    position: absolute;
    left: 290px;
    width: 620px;
    height: 354px;
    border-radius: 4px;
    overflow: hidden;
    box-shadow: 0 14px 30px rgba(0,0,0,.55);
  }
  .card--back { top: 90px; background: var(--card-black); }
  .card--front { top: 540px; }

  .back-logo {
    position: absolute; inset: 0;
    display: flex; flex-direction: column; align-items: center; justify-content: center;
    gap: 18px;
  }
  .back-logo .wordmark {
    font-weight: 600; font-size: 44px; letter-spacing: 6px;
    color: var(--emboss); text-transform: uppercase;
  }
  .back-logo .web {
    font-weight: 400; font-size: 12px; letter-spacing: 6px;
    color: var(--emboss); text-transform: uppercase;
  }

  .front-art { position: absolute; inset: 0; }
  .front-logo {
    position: absolute; left: 320px; top: 108px; width: 300px;
    text-align: center;
    font-weight: 600; font-size: 32px; line-height: 1.2; letter-spacing: 4px;
    color: var(--silver); text-transform: uppercase;
  }
  .identity { position: absolute; left: 34px; top: 48px; color: var(--ink); }
  .identity .name { font-weight: 600; font-size: 21px; letter-spacing: 1px; text-transform: uppercase; }
  .identity .role { font-weight: 500; font-size: 14px; margin-top: 2px; }

  .contact-list { position: absolute; left: 44px; list-style: none; color: var(--ink); }
  .contact-list li {
    display: flex; align-items: center; gap: 8px;
    font-weight: 500; font-size: 14px; line-height: 22px;
  }
  .contact-list svg { width: 13px; height: 13px; flex: none; }
  .social { top: 170px; }
  .direct { top: 240px; }
  .dot { width: 11px; height: 11px; border: 2px solid var(--ink); border-radius: 50%; margin: 0 1px; flex: none; }
</style>
</head>
<body>

<section class="card card--back" aria-label="Card back">
  <div class="back-logo">
    <span class="wordmark">Plumvale Pets</span>
    <span class="web">www.plumvalepets.com</span>
  </div>
</section>

<section class="card card--front" aria-label="Card front">
  <svg class="front-art" viewBox="0 0 620 354" width="620" height="354" aria-hidden="true">
    <defs>
      <linearGradient id="warm" x1="0" y1="0" x2="0.3" y2="1">
        <stop offset="0" stop-color="var(--gold)"/>
        <stop offset="1" stop-color="var(--orange)"/>
      </linearGradient>
      <linearGradient id="silverEdge" x1="0" y1="0" x2="1" y2="1">
        <stop offset="0" stop-color="#ffffff"/>
        <stop offset=".5" stop-color="var(--silver)"/>
        <stop offset="1" stop-color="var(--silver-dark)"/>
      </linearGradient>
    </defs>
    <rect width="620" height="354" fill="url(#warm)"/>
    <path d="M 333.2 0 A 203 203 0 0 0 470 353" fill="none" stroke="url(#silverEdge)" stroke-width="4"/>
    <circle cx="470" cy="150" r="195" fill="var(--card-black)"/>
  </svg>

  <div class="front-logo">Plumvale<br>Pets</div>

  <div class="identity">
    <p class="name">Martin Kolby</p>
    <p class="role">Sales and Marketing</p>
  </div>

  <ul class="contact-list social">
    <li><span class="dot"></span>plumvale pets</li>
    <li><span class="dot"></span>plumvale_pets</li>
  </ul>

  <ul class="contact-list direct">
    <li>
      <svg viewBox="0 0 24 24"><path fill="var(--ink)" d="M6.6 10.8a15 15 0 0 0 6.6 6.6l2.2-2.2c.3-.3.7-.4 1-.2 1.1.4 2.3.6 3.6.6.6 0 1 .4 1 1V20c0 .6-.4 1-1 1A17 17 0 0 1 3 4c0-.6.4-1 1-1h3.5c.6 0 1 .4 1 1 0 1.3.2 2.5.6 3.6.1.3 0 .7-.2 1z"/></svg>
      530-418-2763
    </li>
    <li>
      <svg viewBox="0 0 24 24"><path fill="var(--ink)" d="M2 5h20v14H2zm2 2v.5l8 5 8-5V7z"/></svg>
      info@plumvalepets.com
    </li>
    <li>
      <svg viewBox="0 0 24 24" fill="none" stroke="var(--ink)" stroke-width="2"><circle cx="12" cy="12" r="9"/><path d="M3 12h18M12 3c3 3 3 15 0 18M12 3c-3 3-3 15 0 18"/></svg>
      www.plumvalepets.com
    </li>
  </ul>
</section>

</body>
</html>
```